Logo and Business card design!

Welbrook Estates

We are a Property development and real estate company (needs a logo design).

Welbrook estates is based in Sydney Australia and will be dealing with high net worth individuals with a corporate background. The demographic of clients will be relatively youthful and savvy. We do development finance, property development and some portion of property sales

I'd like the 'Welbrook' part of the name to be strength of the title, with 'property' playing a very minor part, perhaps in tiny font somewhere off to the bottom or side or something

Thank you!

Target Market(s)

25-55 years old

Industry/Entity Type

Real Estate Development

Contact Information for Business Card

Please arrange this information as you see fit

Leon Brightwater
Managing Director
0417 582 273
leon@welbrookestates-example.com.au
www.welbrookestates-example.com.au

Logo Text

Welbrook estates

Font styles to use
Serif

Colors

Designer to choose colors to be used in the design.

Requirements
Must have
• PLEASE VIEW THE UPLOADED IMAGES AND EXAMPLES
• And please put 'property' in small letters at the bottom or to the side. I want it to play a minimalist role, with 'WELBROOK' being the feature
• Colours! Please make sure theyre mostly grey and white with possibly some other dark blue and maybe dark grey
Nice to have
• Please feel free to use whatever colors you like, the suggested colors are something I selected momentarily and dont necessarily reflect strict guidelines
Should not have
• NO pictures or shapes of houses. I dont want the logo design to be so literal in its imagery

```html
<!DOCTYPE html>
<html lang="en">
<head>
<meta charset="utf-8">
<title>Welbrook – Business Card</title>
<link rel="stylesheet" href="https://fonts.googleapis.com/css2?family=Source+Serif+4:opsz,wght@8..60,400;8..60,600&display=swap">
<style>
  :root {
    --bg: #3b3531;
    --card: #131313;
    --gold: #e2a31d;
    --white: #f2f2f2;
    --divider: #3a3a3a;
  }
  * { box-sizing: border-box; margin: 0; padding: 0; }
  html, body { width: 1200px; height: 844px; overflow: hidden; }
  body {
    background: var(--bg);
    font-family: "Source Serif 4", Georgia, serif;
    position: relative;
  }
  .card {
    position: absolute;
    width: 500px;
    height: 286px;
    background: var(--card);
    border-radius: 3px;
    box-shadow: 0 10px 30px rgba(0,0,0,0.45);
  }
  .card-front { left: 70px; top: 320px; }
  .card-back  { left: 630px; top: 238px; }

  .brand {
    position: absolute;
    display: flex;
    align-items: center;
    gap: 14px;
    color: var(--gold);
    font-weight: 400;
    white-space: nowrap;
  }
  .brand-mark {
    width: 34px; height: 34px;
    border-radius: 50%;
    background: var(--gold);
    flex: none;
  }
  .brand-text { display: flex; flex-direction: column; align-items: stretch; }
  .brand-name {
    font-size: 34px;
    line-height: 1;
    letter-spacing: 0.08em;
    text-transform: uppercase;
  }
  .brand-sub {
    display: flex;
    align-items: center;
    gap: 8px;
    margin-top: 4px;
    font-size: 10px;
    line-height: 1;
    letter-spacing: 0.42em;
    text-transform: uppercase;
  }
  .brand-sub::before, .brand-sub::after {
    content: "";
    flex: 1;
    height: 1px;
    background: var(--gold);
  }
  .card-front .brand { left: 50%; top: 52px; transform: translateX(-50%); }
  .card-back .brand  { left: 50%; top: 50%; transform: translate(-50%, -50%); }

  .person {
    position: absolute;
    right: 272px;
    top: 150px;
    text-align: right;
    color: var(--white);
    white-space: nowrap;
  }
  .person-name { color: var(--gold); font-weight: 600; font-size: 18px; line-height: 1.15; }
  .person-role { font-size: 13.5px; line-height: 1.25; }
  .person-address { font-size: 13.5px; line-height: 1.25; margin-top: 14px; }

  .divider {
    position: absolute;
    left: 240px; top: 150px;
    width: 1px; height: 98px;
    background: var(--divider);
  }
  .contact {
    position: absolute;
    left: 252px; top: 150px;
    list-style: none;
    color: var(--white);
    font-size: 12px;
    white-space: nowrap;
  }
  .contact li { display: flex; align-items: center; gap: 8px; line-height: 20px; }
  .contact svg { width: 11px; height: 11px; fill: var(--gold); flex: none; }
</style>
</head>
<body>

<section class="card card-front" aria-label="Business card front">
  <div class="brand">
    <span class="brand-mark"></span>
    <span class="brand-text">
      <span class="brand-name">Welbrook</span>
      <span class="brand-sub">Property</span>
    </span>
  </div>

  <div class="person">
    <p class="person-name">Leon Brightwater</p>
    <p class="person-role">Managing Director</p>
    <p class="person-address">12345, Address Goes Here<br>Country Name, 123456</p>
  </div>

  <div class="divider"></div>

  <ul class="contact">
    <li>
      <svg viewBox="0 0 12 12" aria-hidden="true"><path d="M2.5 1l2 2.2-1 1.3c.7 1.5 1.9 2.7 3.4 3.4l1.3-1 2.2 2-1 2C5 10.5 1.5 7 1 2z"/></svg>
      0417 582 273
    </li>
    <li>
      <svg viewBox="0 0 12 12" aria-hidden="true"><rect x="3" y="1" width="6" height="3"/><rect x="1" y="4.5" width="10" height="6.5" rx="1"/></svg>
      02 9187 4420
    </li>
    <li>
      <svg viewBox="0 0 12 12" aria-hidden="true"><path d="M1 2.5h10v1L6 7 1 3.5zM1 5l5 3.5L11 5v4.5H1z"/></svg>
      leon@welbrookestates-example.com.au
    </li>
    <li>
      <svg viewBox="0 0 12 12" aria-hidden="true"><circle cx="6" cy="6" r="5"/></svg>
      www.welbrookestates-example.com.au
    </li>
  </ul>
</section>

<section class="card card-back" aria-label="Business card back">
  <div class="brand">
    <span class="brand-mark"></span>
    <span class="brand-text">
      <span class="brand-name">Welbrook</span>
      <span class="brand-sub">Property</span>
    </span>
  </div>
</section>

</body>
</html>
```